Website design for management consulting firm

We need a web design for a new consulting company based in Boston, MA called "Quillmoor Ridge Consulting." This webpage will be simple home page, with a "contact us" page, that describes the services of the consulting firm. The company provides strategic planning, business assessment, process re-designs, and other management consulting functions. I would like the website to look high-tech. A logo was already created via Artsy Hive.

Target Market(s)

Other business owners across a wide spectrum of industries - from IT to retail.

Industry/Entity Type

It Company

Number of Pages Required

3 page

Colors
0455a3
ffffff

Requirements
Must have
• Front page that provides generic text / overview of the firm. A "services" tab that describes consulting services. A "contact us" tab that provides either a form to contact us or just the contact email address of the company. info@quillmoorridgeconsulting.example

```html
<!DOCTYPE html>
<html lang="en">
<head>
<meta charset="utf-8">
<title>Quillmoor Ridge Consulting – Services</title>
<link rel="stylesheet" href="https://fonts.googleapis.com/css2?family=Open+Sans:wght@300;400;600;700&display=swap">
<style>
  :root {
    --blue: #0455a3;
    --blue-light: #3573b5;
    --white: #ffffff;
    --ink: #222222;
    --text: #555555;
    --page-bg: #f3f3f3;
    --footer-bg: #f8f8f8;
    --rule: #c9c9c9;
    --bar: #444444;
  }
  * { box-sizing: border-box; margin: 0; padding: 0; }
  html, body { width: 1200px; height: 1184px; overflow: hidden; }
  body { position: relative; font-family: "Open Sans", sans-serif; background: var(--page-bg); color: var(--text); }
  .abs { position: absolute; }

  /* header */
  .site-header { left: 0; top: 0; width: 1200px; height: 93px; background: var(--white); }
  .brand { left: 161px; top: 22px; display: flex; align-items: center; gap: 10px; }
  .brand-mark { width: 46px; height: 50px; background: var(--blue); }
  .brand-name { font-size: 20px; font-weight: 600; color: var(--ink); letter-spacing: -0.3px; }
  .main-nav a { position: absolute; top: 0; height: 93px; line-height: 20px; padding-top: 52px; font-size: 16px; font-weight: 300; color: var(--blue); text-decoration: none; }
  .main-nav a.active { background: var(--blue); color: var(--white); width: 97px; text-align: center; }

  /* hero */
  .hero { left: 0; top: 93px; width: 1200px; height: 240px; background: linear-gradient(90deg, #1d2a34 0%, #4e6e80 45%, #5f8191 70%, #2c3d48 100%); }
  .hero-title { left: 161px; top: 176px; font-size: 35px; font-weight: 600; color: var(--white); line-height: 44px; }
  .hero-rule-top { left: 161px; top: 224px; width: 267px; height: 1px; background: var(--white); }
  .hero-rule-side { left: 234px; top: 224px; width: 1px; height: 63px; background: var(--white); }
  .hero-rule-bottom { left: 234px; top: 286px; width: 394px; height: 1px; background: var(--white); }
  .hero-kicker { left: 253px; top: 232px; font-size: 19px; font-weight: 300; color: var(--white); }
  .hero-tagline { left: 253px; top: 253px; font-size: 21px; font-weight: 700; color: var(--white); }

  /* service tiles */
  .service-tiles { left: 161px; top: 333px; width: 878px; height: 185px; display: flex; }
  .tile { width: 219.5px; height: 185px; display: flex; flex-direction: column; align-items: center; color: var(--white); }
  .tile.dark { background: var(--blue); }
  .tile.light { background: var(--blue-light); }
  .tile svg { margin-top: 40px; width: 62px; height: 62px; }
  .tile-label { margin-top: 20px; font-size: 14px; font-weight: 700; letter-spacing: 0.2px; white-space: nowrap; }
  .tile-pointer { left: 264px; top: 518px; width: 0; height: 0; border-left: 6px solid transparent; border-right: 6px solid transparent; border-top: 10px solid var(--blue); }

  /* detail */
  .detail-bar { left: 161px; top: 566px; width: 3px; height: 32px; background: var(--blue); }
  .detail-title { left: 176px; top: 562px; font-size: 27px; font-weight: 700; color: var(--blue); line-height: 38px; }
  .detail-copy { left: 160px; top: 617px; width: 380px; font-size: 12.5px; font-weight: 300; line-height: 21px; color: var(--text); }
  .btn-more { left: 161px; top: 716px; width: 94px; height: 26px; background: var(--blue); color: var(--white); font-size: 12.5px; line-height: 26px; text-align: center; }
  .detail-photo { left: 600px; top: 551px; width: 439px; height: 282px; background: linear-gradient(135deg, #c7d3dd 0%, #8fa3b6 45%, #d8d4cf 75%, #a9b7c4 100%); }

  /* footer */
  .footer-rule { left: 161px; top: 885px; width: 878px; height: 1px; background: var(--rule); }
  .site-footer { left: 0; top: 886px; width: 1200px; height: 238px; background: var(--footer-bg); }
  .footer-brand { left: 170px; top: 931px; display: flex; align-items: center; gap: 8px; }
  .footer-brand .brand-mark { width: 32px; height: 34px; }
  .footer-brand .brand-name { font-size: 15px; }
  .footer-brand-rule { left: 162px; top: 986px; width: 225px; height: 1px; background: var(--rule); }
  .newsletter-title { left: 169px; top: 1008px; font-size: 16px; font-weight: 400; color: var(--blue); }
  .newsletter-note { left: 172px; top: 1042px; font-size: 12.5px; color: var(--ink); }
  .newsletter-input { left: 169px; top: 1064px; width: 178px; height: 32px; border: 1px solid #dddddd; background: var(--white); font-size: 10px; color: var(--ink); padding-left: 10px; line-height: 30px; }
  .newsletter-go { left: 347px; top: 1064px; width: 40px; height: 32px; background: var(--blue); color: var(--white); font-size: 16px; text-align: center; line-height: 32px; }
  .footer-heading { top: 929px; font-size: 16px; font-weight: 700; color: var(--blue); padding-bottom: 2px; border-bottom: 1px solid var(--blue); letter-spacing: 0.2px; }
  .footer-list { list-style: none; font-size: 12.5px; color: var(--ink); line-height: 23px; }
  .social-row { display: flex; align-items: center; height: 29px; }
  .social-box { width: 26px; height: 26px; background: var(--blue); margin-right: 13px; }

  .copyright-bar { left: 0; top: 1124px; width: 1200px; height: 60px; background: var(--bar); color: var(--white); font-size: 13px; text-align: center; line-height: 60px; }
</style>
</head>
<body>

<header class="abs site-header">
  <div class="abs brand"><span class="brand-mark"></span><span class="brand-name">Quillmoor Ridge Consulting</span></div>
  <nav class="main-nav">
    <a style="left:496px">HOME</a>
    <a style="left:579px">ABOUT</a>
    <a style="left:667px">BLOG</a>
    <a style="left:745px">NEWS</a>
    <a class="active" style="left:811px">SERVICES</a>
    <a style="left:925px">CONTACT US</a>
  </nav>
</header>

<section class="abs hero" role="img" aria-label="Business team silhouetted against large office windows"></section>
<h1 class="abs hero-title">OUR SERVICES</h1>
<div class="abs hero-rule-top"></div>
<div class="abs hero-rule-side"></div>
<div class="abs hero-rule-bottom"></div>
<p class="abs hero-kicker">Step in to a business</p>
<p class="abs hero-tagline">Its our duty to lead you to success</p>

<div class="abs service-tiles">
  <div class="tile dark">
    <svg viewBox="0 0 62 62" fill="none" stroke="#fff" stroke-width="2.6">
      <circle cx="10" cy="10" r="6"/><circle cx="31" cy="8" r="6"/><circle cx="52" cy="10" r="6"/>
      <circle cx="10" cy="52" r="6"/><circle cx="31" cy="54" r="6"/><circle cx="52" cy="52" r="6"/>
      <rect x="21" y="24" width="20" height="14"/>
      <path d="M10 16v8h11M52 16v8H41M31 14v10M10 46v-8h11M52 46v-8H41M31 38v10"/>
    </svg>
    <span class="tile-label">STRATEGIC PLANNING</span>
  </div>
  <div class="tile light">
    <svg viewBox="0 0 62 62" fill="none" stroke="#fff" stroke-width="3">
      <circle cx="31" cy="31" r="26" stroke-dasharray="4 3"/>
      <circle cx="31" cy="31" r="19"/>
      <circle cx="31" cy="31" r="10"/>
      <path d="M31 12v9M31 41v9M12 31h9M41 31h9"/>
    </svg>
    <span class="tile-label">PROCESS RE-DESIGNS</span>
  </div>
  <div class="tile dark">
    <svg viewBox="0 0 62 62" fill="none" stroke="#fff" stroke-width="2.6">
      <path d="M3 4h56"/><rect x="7" y="4" width="48" height="34"/>
      <path d="M14 30l9-8 8 5 14-13" /><circle cx="23" cy="22" r="2"/><circle cx="31" cy="27" r="2"/><circle cx="45" cy="14" r="2"/>
      <path d="M31 38v12M31 50l-14 8M31 50l14 8M31 50v8"/>
    </svg>
    <span class="tile-label">BUSINESS ASSESSMENT</span>
  </div>
  <div class="tile light">
    <svg viewBox="0 0 62 62" fill="#fff">
      <circle cx="12" cy="10" r="5"/><circle cx="50" cy="10" r="5"/>
      <rect x="7" y="17" width="9" height="20" rx="2"/><rect x="46" y="17" width="9" height="20" rx="2"/>
      <rect x="2" y="22" width="3" height="28"/><rect x="57" y="22" width="3" height="28"/>
      <rect x="5" y="37" width="18" height="4"/><rect x="39" y="37" width="18" height="4"/>
      <rect x="20" y="28" width="22" height="28"/>
    </svg>
    <span class="tile-label">MANAGEMENT CONSULTING</span>
  </div>
</div>
<div class="abs tile-pointer"></div>

<div class="abs detail-bar"></div>
<h2 class="abs detail-title">STRATEGIC PLANNING</h2>
<p class="abs detail-copy">Lorem Ipsum is simply dummy text of the printing and typesetting industry. Lorem Ipsum has been the industry's standard dummy text ever since the 1500s, when an unknown printer took a galley of type and scrambled it to make a type specimen book.</p>
<div class="abs btn-more">READ MORE</div>
<div class="abs detail-photo" role="img" aria-label="Consultants in discussion around a meeting table"></div>

<div class="abs footer-rule"></div>
<footer class="abs site-footer"></footer>
<div class="abs footer-brand"><span class="brand-mark"></span><span class="brand-name">Quillmoor Ridge Consulting</span></div>
<div class="abs footer-brand-rule"></div>
<h3 class="abs newsletter-title">NEWSLETTER</h3>
<p class="abs newsletter-note">Sign up Your Newsletter</p>
<div class="abs newsletter-input">E-mail</div>
<div class="abs newsletter-go">GO</div>

<h3 class="abs footer-heading" style="left:439px">QUICK LINKS</h3>
<ul class="abs footer-list" style="left:443px; top:963px">
  <li>HOME</li><li>About</li><li>Blog</li><li>News</li><li>Services</li><li>Contact us</li>
</ul>

<h3 class="abs footer-heading" style="left:580px">CONTACT DETAILS</h3>
<ul class="abs footer-list" style="left:583px; top:966px">
  <li>Quillmoor Ridge Consulting</li>
  <li>#7, Linden Row, Harbor Quarter</li>
  <li>Boston, Massachusetts, USA</li>
  <li>Phone : +000 5550 147</li>
  <li>Email : info@quillmoorridgeconsulting.example</li>
</ul>

<h3 class="abs footer-heading" style="left:880px">FOLLW US ON</h3>
<div class="abs footer-list" style="left:887px; top:965px">
  <div class="social-row"><span class="social-box"></span>friendnet</div>
  <div class="social-row"><span class="social-box"></span>chirpline</div>
  <div class="social-row"><span class="social-box"></span>vidcast</div>
  <div class="social-row"><span class="social-box"></span>circlespace +</div>
</div>

<div class="abs copyright-bar">© 2015 Quillmoor Ridge Consulting. allright Reserved</div>

</body>
</html>
```